(3) Image Sliders for Wordpress Site

We need to update our WP slides on a corporate website. We are an IP communications solution provider to government and enterprises. Our website is www.velunor.com. You can see the existing sliders for size. I like crisp, professional-looking slides (NOT like the ones currently displayed). They shouldn't look like stock art/photos --- they should look original. They should also use current/new artistic methods (i.e. the "latest" concepts in design).

The Images should be JPG format, 946 x 376.

Use colors from logo on website, but don't completely restrict yourself. Photos are OK.

Slide Text:
Slide 1:
Main Message: "Creative solutions for government"
Bulleted text (use any kind of bullet or separator you want):
-Reduce FTE costs and eliminate capital expenses
-Dramatically improve community services
-Make government accessible for all constituents on all devices

Slide 2:
Main Message: "Corvane Systems Deployment"
-Take advantage of dramatic cost savings vs. going direct
-Leverage VeLUNOR's 13 years of experience
-Deploy On-Premises for optimal security, control and customization

Slide 3:
Main Message: "Enterprise Unified Communications"
-Revolutionize the way your people communicate and collaborate
-Realize instant cost savings by replacing multiple systems with one unified platform
-Bring everyone together, no matter where they are.

Hi Everyone I appreciate your submissions, but they are full of stock graphics and stuff I could have done..Looking for something more creative and unique to us. Since we're primarily a government/enterprise contractor, it doesn't have to be artsy or cute, but it does need to rise above the typical stock stuff i'm seeing. More information: -The Corvane Systems logo should go on the Corvane Systems-related slide -If you need more relevant logos or images let me know. Here are some slides that I like: http://brelmacraft.com/images/2014/0710-1/unslider.jpg http://brelmacraft.com/images/2014/0710-1/superslides.jpg http://www.tovelpikstudio.com/wp-content/uploads/2012/02/jquerysliders10b.jpg something like this with layered text for our gov slider, but NYC skyline: http://www.tovelpikstudio.com/wp-content/uploads/2012/02/jquerysliders18.jpg

Communications

```html
<!DOCTYPE html>
<html lang="en">
<head>
<meta charset="utf-8">
<title>Creative Solutions for Government</title>
<link rel="stylesheet" href="https://fonts.googleapis.com/css2?family=Oswald:wght@300;600&family=Roboto+Condensed:wght@300;400;700&display=swap">
<style>
  :root {
    --bg-light: #f4f4f4;
    --bg-mid: #e6e6e6;
    --ink: #1e1e1e;
    --white: #ffffff;
    --blue: #1aa3df;
    --orange: #f6ab2a;
    --purple: #b14f9a;
    --green: #7cbf3f;
    --dots: #3a8fd0;
    --brand-blue: #1e4f9c;
  }
  html, body {
    margin: 0;
    padding: 0;
    width: 1200px;
    height: 477px;
    overflow: hidden;
    background: var(--bg-light);
  }
  .slide {
    position: relative;
    width: 1200px;
    height: 477px;
    overflow: hidden;
    background: radial-gradient(ellipse at 50% 35%, var(--bg-light) 0%, var(--bg-mid) 100%);
  }
  .slide svg { display: block; }
  .headline {
    font-family: "Oswald", sans-serif;
    font-size: 40px;
    letter-spacing: 1px;
    fill: var(--ink);
  }
  .headline .strong { font-weight: 600; }
  .headline .light { font-weight: 300; }
  .bubble { fill: var(--white); filter: drop-shadow(0 2px 6px rgba(0,0,0,0.25)); }
  .ring-blue { fill: var(--blue); }
  .ring-orange { fill: var(--orange); }
  .ring-purple { fill: var(--purple); }
  .ring-green { fill: var(--green); }
  .link-dots { fill: none; stroke: var(--dots); stroke-width: 1.6; stroke-dasharray: 1.5 4; stroke-linecap: round; }
  .point {
    font-family: "Roboto Condensed", sans-serif;
    font-weight: 300;
    font-size: 19px;
    fill: var(--ink);
    text-anchor: middle;
  }
  .icon { fill: var(--ink); stroke: none; }
  .icon-line { fill: none; stroke: var(--ink); stroke-width: 2.4; }
  .brand-name {
    font-family: "Roboto Condensed", sans-serif;
    font-weight: 700;
    font-size: 19px;
    fill: var(--brand-blue);
    text-anchor: middle;
  }
</style>
</head>
<body>
<div class="slide">
  <svg width="1200" height="477" viewBox="0 0 946 376" xmlns="http://www.w3.org/2000/svg">
    <text class="headline" x="473" y="62" text-anchor="middle"><tspan class="strong">CREATIVE SOLUTIONS</tspan><tspan class="light"> FOR GOVERNMENT</tspan></text>

    <path class="link-dots" d="M150 150 Q 300 80 470 120"/>
    <path class="link-dots" d="M590 160 Q 640 110 700 125"/>
    <path class="link-dots" d="M770 376 Q 820 330 850 320"/>

    <circle class="ring-blue" cx="238" cy="302" r="130"/>
    <circle class="ring-orange" cx="452" cy="215" r="82"/>
    <circle class="ring-purple" cx="566" cy="312" r="152"/>
    <circle class="ring-green" cx="780" cy="282" r="120"/>

    <circle class="bubble" cx="262" cy="270" r="125"/>
    <circle class="bubble" cx="576" cy="292" r="140"/>
    <circle class="bubble" cx="787" cy="258" r="124"/>
    <circle class="bubble" cx="117" cy="185" r="63"/>

    <g class="brand">
      <text class="brand-name" x="117" y="190">VeLUNOR</text>
    </g>

    <g class="devices-icon">
      <rect class="icon-line" x="253" y="175" width="46" height="30" rx="2"/>
      <line class="icon-line" x1="270" y1="213" x2="284" y2="213"/>
      <line class="icon-line" x1="277" y1="205" x2="277" y2="213"/>
      <rect x="234" y="180" width="24" height="44" rx="3" fill="var(--white)" stroke="var(--ink)" stroke-width="2.4"/>
      <line class="icon-line" x1="242" y1="218" x2="250" y2="218"/>
    </g>
    <text class="point" x="266" y="272">Make government</text>
    <text class="point" x="266" y="295">accessible for all</text>
    <text class="point" x="266" y="318">constituents on all</text>
    <text class="point" x="266" y="341">devices</text>

    <g class="decline-icon">
      <rect class="icon" x="545" y="217" width="7" height="30"/>
      <rect class="icon" x="556" y="224" width="7" height="23"/>
      <rect class="icon" x="567" y="230" width="7" height="17"/>
      <rect class="icon" x="578" y="235" width="7" height="12"/>
      <path class="icon-line" d="M545 206 L572 214"/>
      <path class="icon" d="M570 208 L584 217 L568 221 Z"/>
    </g>
    <text class="point" x="563" y="296">Reduce FTE costs</text>
    <text class="point" x="563" y="319">and eliminate</text>
    <text class="point" x="563" y="342">capital expenses</text>

    <g class="community-icon">
      <circle class="icon" cx="786" cy="180" r="6"/>
      <path class="icon" d="M776 202 a10 9 0 0 1 20 0 Z"/>
      <circle class="icon" cx="769" cy="190" r="5"/>
      <path class="icon" d="M761 209 a8 8 0 0 1 16 0 Z"/>
      <circle class="icon" cx="803" cy="190" r="5"/>
      <path class="icon" d="M795 209 a8 8 0 0 1 16 0 Z"/>
      <circle class="icon" cx="786" cy="203" r="5"/>
      <path class="icon" d="M777 214 a9 7 0 0 1 18 0 Z"/>
    </g>
    <text class="point" x="784" y="252">Dramatically improve</text>
    <text class="point" x="784" y="275">community services</text>
  </svg>
</div>
</body>
</html>
```